Residential Construction Company needs flyer designed.

We need a flyer design for a residential Rain Gutter and Screen room company. We have over 50 years in the remodeling industry and service all of Middle Georgia. We want the brochure to highlight our wonderful managerial staff to our great instillation crews. We also want to showcase the high-quality products that we use, gutter, leaf protection, screen rooms and sunrooms and the quality craftsmanship homeowners will receive when they choose to go with our company.

```html
<!DOCTYPE html>
<html lang="en">
<head>
<meta charset="utf-8">
<title>Harlan Gutters &amp; Exteriors Flyer</title>
<link href="https://fonts.googleapis.com/css2?family=Crimson+Text:wght@400;600;700&display=swap" rel="stylesheet">
<style>
:root{
  --page-bg:#e8ecef;
  --paper:#ffffff;
  --brand-blue:#1e6db3;
  --deep-blue:#0f4f87;
  --navy-text:#143a66;
  --violet-band:#3d3e8e;
  --body-text:#2a3a4d;
  --muted:#8a8f96;
}
*{margin:0;padding:0;box-sizing:border-box}
html,body{width:1200px;height:2416px;overflow:hidden;background:var(--page-bg);font-family:"Crimson Text",Georgia,serif}
.flyer{position:absolute;left:40px;top:335px;width:1120px;height:1745px;background:var(--paper);box-shadow:0 10px 40px rgba(0,0,0,.18);overflow:hidden}
.abs{position:absolute}
.brand-name{left:60px;top:95px;width:360px;color:var(--brand-blue);font-weight:700;font-size:46px;line-height:1.05;display:flex;align-items:center;gap:14px}
.brand-name .mark{width:34px;height:34px;border-radius:50%;background:var(--brand-blue);flex:none}
.photo{position:absolute}
.photo-sunroom{left:0;top:265px;width:453px;height:356px;background:linear-gradient(160deg,#9aa5ae 0%,#e9ebe8 40%,#7e8a6a 80%,#5b6d3e 100%)}
.photo-brick{left:0;top:626px;width:453px;height:331px;background:linear-gradient(170deg,#dfe6ee 0%,#a49a90 45%,#7d7064 80%,#4e4a45 100%)}
.photo-deck{left:8px;top:974px;width:210px;height:294px;background:linear-gradient(180deg,#dfe8f2 0%,#4a5f86 40%,#7c5a44 70%,#6aa4c8 100%)}
.photo-guard{left:243px;top:974px;width:210px;height:294px;background:linear-gradient(120deg,#9dc06a 0%,#b6b8b8 45%,#5e6264 100%)}
.hero{left:467px;top:0;width:653px;height:621px;background:linear-gradient(180deg,#9cc0de 0%,#d9dcdc 30%,#b9bcbf 52%,#3f6e93 75%,#1f5b86 100%)}
.hero-copy{left:497px;top:345px;color:#fff}
.hero-kicker{font-size:40px;font-weight:400;line-height:1}
.hero-title{font-size:60px;font-weight:700;line-height:1.1;margin-top:6px}
.hero-years{left:497px;top:524px;width:385px;height:64px;background:#fff;clip-path:polygon(0 0,92% 0,100% 100%,0 100%)}
.hero-years span{display:block;padding:4px 0 0 14px;font-size:48px;color:var(--brand-blue);line-height:1.1}
.section-title{color:var(--brand-blue);font-weight:700;font-size:34px}
.services-title{left:492px;top:668px}
.service{position:absolute;top:727px;width:200px;text-align:center}
.service .icon{width:72px;height:72px;margin:0 auto;display:block}
.service h3{color:var(--brand-blue);font-weight:600;font-size:23px;margin-top:14px;line-height:1.1}
.service p{color:var(--body-text);font-size:17px;line-height:1.25;margin-top:6px}
.colors-title{left:492px;top:948px}
.swatches{left:484px;top:1007px;width:600px;display:grid;grid-template-columns:repeat(8,62px);column-gap:12px;row-gap:26px}
.swatch div{width:62px;height:64px}
.swatch span{display:block;font-size:9px;color:var(--muted);margin-top:3px;white-space:nowrap}
.specialty-title{left:57px;top:1316px;font-size:32px;font-weight:600;color:var(--brand-blue)}
.product{position:absolute;top:1370px;width:190px;height:191px;box-shadow:0 6px 8px rgba(20,30,80,.25)}
.product .img{width:100%;height:141px}
.product .label{height:50px;background:var(--violet-band);color:#fff;font-size:17px;line-height:1.1;display:flex;align-items:center;justify-content:center;text-align:center}
.contact-title{left:57px;top:1600px;font-size:26px;font-weight:600;color:var(--navy-text)}
.phone-band{left:0;top:1637px;width:453px;height:67px;background:var(--brand-blue);clip-path:polygon(0 0,100% 0,96% 100%,0 100%);color:#fff;font-size:50px;display:flex;align-items:center;padding-left:55px;gap:12px;line-height:1}
.info{position:absolute;top:1650px;font-size:19px;line-height:1.35;color:var(--navy-text);display:flex;gap:8px}
.info svg{flex:none;margin-top:4px}
</style>
</head>
<body>
<main class="flyer">
  <div class="abs brand-name"><span class="mark"></span><span>Harlan Gutters &amp; Exteriors</span></div>

  <div class="photo photo-sunroom" role="img" aria-label="White screened sunroom addition on a brick home"></div>
  <div class="photo photo-brick" role="img" aria-label="Brick house corner with arched screened porch and seamless gutters"></div>
  <div class="photo photo-deck" role="img" aria-label="Blue home with covered deck beside a pool"></div>
  <div class="photo photo-guard" role="img" aria-label="Close view of perforated gutter guard along a roof edge"></div>

  <div class="photo hero" role="img" aria-label="Large white two-story home with slate roof and lawn"></div>
  <div class="abs hero-copy">
    <div class="hero-kicker">Your Trusted Partner in</div>
    <div class="hero-title">Quality Rain Gutter<br>&amp; Screen Solutions</div>
  </div>
  <div class="abs hero-years"><span>for Over 50 Years</span></div>

  <h2 class="abs section-title services-title">Our Services</h2>
  <div class="service" style="left:466px">
    <svg class="icon" viewBox="0 0 72 72"><circle cx="36" cy="36" r="33" fill="none" stroke="var(--brand-blue)" stroke-width="2.5"/><path d="M21 37 36 22 51 37H46V51H26V37Z" fill="var(--brand-blue)"/><rect x="32" y="41" width="8" height="10" fill="#fff"/></svg>
    <h3>Gutter Systems</h3><p>Avoid Water Damage<br>with Proper Drainage</p>
  </div>
  <div class="service" style="left:677px">
    <svg class="icon" viewBox="0 0 72 72"><circle cx="36" cy="36" r="33" fill="none" stroke="var(--brand-blue)" stroke-width="2.5"/><circle cx="37" cy="34" r="15" fill="none" stroke="var(--brand-blue)" stroke-width="3"/><path d="M20 24c-3 8 4 22 16 26l4-5-5-4-3 2c-4-2-7-7-7-11l3-2-3-6Z" fill="var(--brand-blue)"/><text x="37" y="39" font-size="13" font-family="Arial,sans-serif" font-weight="700" text-anchor="middle" fill="var(--brand-blue)">24</text></svg>
    <h3>Patio Covers</h3><p>Built for entertaining and<br>shelter from the sun</p>
  </div>
  <div class="service" style="left:887px;top:727px">
    <svg class="icon" viewBox="0 0 72 72"><circle cx="36" cy="36" r="33" fill="none" stroke="var(--brand-blue)" stroke-width="2.5"/><path d="M20 34 36 28 52 34V48L36 54 20 48Z" fill="var(--brand-blue)"/><path d="M36 14V28M30 20 36 14 42 20" stroke="var(--brand-blue)" stroke-width="3" fill="none"/><path d="M20 34 36 40 52 34" stroke="#fff" stroke-width="2" fill="none"/></svg>
    <h3 style="margin-top:22px">Screenroom</h3><p>Enjoy Your Patio with<br>a Screen Room</p>
  </div>

  <h2 class="abs section-title colors-title">Color Options</h2>
  <div class="abs swatches">
    <div class="swatch"><div style="background:#f7f8f9;border:1px solid #eee"></div><span>Bright White</span></div>
    <div class="swatch"><div style="background:#f1f2f3;border:1px solid #eee"></div><span>Pearl White</span></div>
    <div class="swatch"><div style="background:#f0e3cb"></div><span>Almond</span></div>
    <div class="swatch"><div style="background:#dbb48d"></div><span>Antique Ivory</span></div>
    <div class="swatch"><div style="background:#050505"></div><span>Black</span></div>
    <div class="swatch"><div style="background:#444547"></div><span>Charcoal</span></div>
    <div class="swatch"><div style="background:#ddd6c7"></div><span>Eggshell</span></div>
    <div class="swatch"><div style="background:#2d4f43"></div><span>Forest Green</span></div>
    <div class="swatch"><div style="background:#a7a5a2"></div><span>Clay</span></div>
    <div class="swatch"><div style="background:#8e6448"></div><span>Cocoa Brown</span></div>
    <div class="swatch"><div style="background:#bdbdbd"></div><span>Colonial Gray</span></div>
    <div class="swatch"><div style="background:linear-gradient(90deg,#a9541c,#f0b47a,#b8652a)"></div><span>Copper</span></div>
    <div class="swatch"><div style="background:#f6f0e6"></div><span>Cream</span></div>
    <div class="swatch"><div style="background:#8c918c"></div><span>Dove Gray</span></div>
    <div class="swatch"><div style="background:#a61f24"></div><span>Scarlet Red</span></div>
    <div class="swatch"><div style="background:#68625a"></div><span>Terratone</span></div>
    <div class="swatch"><div style="background:#dedcc8"></div><span>Linen</span></div>
    <div class="swatch"><div style="background:#4d3b20"></div><span>Musket Brown</span></div>
    <div class="swatch"><div style="background:#b7c0b6"></div><span>Sage Gray</span></div>
    <div class="swatch"><div style="background:#6b2a0a"></div><span>Royal Brown</span></div>
    <div class="swatch"><div style="background:#5a8aa8"></div><span>Traditional Blue</span></div>
    <div class="swatch"><div style="background:#55555a"></div><span>Tuxedo Gray</span></div>
    <div class="swatch"><div style="background:#d6c69c"></div><span>Wicker</span></div>
  </div>

  <h2 class="abs specialty-title">Harlan Gutters &amp; Exteriors specializes in the quality installation of:</h2>
  <div class="product" style="left:57px"><div class="img" role="img" aria-label="Gutter protection mesh panel" style="background:linear-gradient(160deg,#fff 30%,#6e6a60 60%,#c9c4b8 100%)"></div><div class="label">ClearFlow Gutter<br>Protection System</div></div>
  <div class="product" style="left:261px"><div class="img" role="img" aria-label="Brick home with seamless gutters and downspouts" style="background:linear-gradient(170deg,#cbd6e0 0%,#8f6e58 50%,#5d6e3e 100%)"></div><div class="label">Seamless Aluminum<br>Gutters &amp; Downspouts</div></div>
  <div class="product" style="left:465px"><div class="img" role="img" aria-label="Leaves being cleared from a gutter" style="background:linear-gradient(150deg,#b9b2a2 0%,#8d7a57 50%,#6f6e6a 100%)"></div><div class="label">Gutter Cleaning</div></div>
  <div class="product" style="left:669px"><div class="img" role="img" aria-label="Covered patio with white ceiling overlooking a yard" style="background:linear-gradient(180deg,#f1f3f2 0%,#d2d7d2 50%,#6c9a52 80%,#eaeeea 100%)"></div><div class="label">Patio Covers</div></div>
  <div class="product" style="left:873px"><div class="img" role="img" aria-label="Brick home with gutter covers on the roofline" style="background:linear-gradient(175deg,#a7c4e2 0%,#5a6270 45%,#8f6a52 75%,#6f8a4a 100%)"></div><div class="label">Gutter Covers</div></div>

  <div class="abs contact-title">Contact Harlan Gutters &amp; Exteriors</div>
  <div class="abs phone-band">
    <svg width="26" height="30" viewBox="0 0 26 30"><path d="M5 2 10 1 12 9 8 11C9 16 11 19 15 22L18 19 25 23 23 28C14 30 2 17 5 2Z" fill="#fff"/></svg>
    <span>(478) 555-0142</span>
  </div>
  <div class="info" style="left:462px">
    <svg width="16" height="16" viewBox="0 0 16 16"><path d="M1 8 8 1 15 8H13V15H3V8Z" fill="var(--brand-blue)"/></svg>
    <span>412 Maple Ridge Pkwy,<br>Oakdale, GA 31000</span>
  </div>
  <div class="info" style="left:718px">
    <svg width="16" height="34" viewBox="0 0 16 34"><rect x="1" y="3" width="14" height="10" fill="var(--brand-blue)"/><path d="M1 3 8 9 15 3" stroke="#fff" stroke-width="1.5" fill="none"/><circle cx="8" cy="26" r="6.5" fill="none" stroke="var(--brand-blue)" stroke-width="1.8"/><path d="M1.5 26H14.5M8 19.5C5 23 5 29 8 32.5M8 19.5C11 23 11 29 8 32.5" stroke="var(--brand-blue)" stroke-width="1.2" fill="none"/></svg>
    <span>info@harlanguttersandexteriors.com<br>www.harlanguttersandexteriors.com</span>
  </div>
</main>
</body>
</html>
```